MRW Snack Box for Printed Packaging

This is a TVW style 2 piece snack box. We have a jpeg logo and need it to be applied to the box along with some form of creative design. I have uploaded the keyline for the package. Please lay out the logo and design on this. Please bear in mind that the carton will be folded and appear like the photo which is also uploaded

Target Market(s)

General consumers in St. Lucia in the caribbean

Colors
EB3D1F
EC4F4E
F09395
F8D3D4
FCEDEE

```html
<!DOCTYPE html>
<html lang="en">
<head>
<meta charset="utf-8">
<title>MRW Snack Box – Printed Packaging Layout</title>
<link rel="stylesheet" href="https://fonts.googleapis.com/css2?family=Fredoka:wght@700&display=swap">
<style>
  :root {
    --brand-red: #EB3D1F;
    --band-red: #EC3539;
    --soft-red: #EC4F4E;
    --pink: #F09395;
    --blush: #F8D3D4;
    --mist: #FCEDEE;
    --paper: #FFFFFF;
    --keyline: #29ABE2;
    --mascot-white: #F4F6FB;
  }
  html, body {
    margin: 0;
    padding: 0;
    width: 1200px;
    height: 500px;
    overflow: hidden;
    background: var(--paper);
  }
  .dieline {
    display: block;
    width: 1200px;
    height: 500px;
  }
  .top-band { fill: var(--band-red); }
  .check-band { fill: url(#checkTone); }
  .mascot-area { fill: url(#mascotTone); }
  .brand-name {
    font-family: "Fredoka", "Arial Rounded MT Bold", sans-serif;
    font-weight: 700;
    font-size: 74px;
    fill: var(--brand-red);
    letter-spacing: 1px;
  }
  .cut-line, .fold-line {
    fill: none;
    stroke: var(--keyline);
    stroke-width: 2;
  }
  .fold-line { stroke-dasharray: 90 18; }
</style>
</head>
<body>
<svg class="dieline" viewBox="0 0 2560 1067" preserveAspectRatio="none" xmlns="http://www.w3.org/2000/svg">
  <defs>
    <linearGradient id="checkTone" x1="0" x2="1" y1="0" y2="0">
      <stop offset="0" stop-color="#F09395"/>
      <stop offset="1" stop-color="#EC4F4E"/>
    </linearGradient>
    <linearGradient id="mascotTone" x1="0" x2="0" y1="0" y2="1">
      <stop offset="0" stop-color="#F4F6FB"/>
      <stop offset="0.65" stop-color="#F8D3D4"/>
      <stop offset="1" stop-color="#E03236"/>
    </linearGradient>

    <g id="keyline-half">
      <!-- glue flap -->
      <polyline class="cut-line" points="291,203 234,218 234,340 291,397"/>
      <polyline class="cut-line" points="291,400 234,400 234,590 291,648"/>
      <!-- side panel top and gable -->
      <polyline class="cut-line" points="930,203 1270,203 1318,180"/>
      <polyline class="fold-line" points="930,397 1124,203 1318,397"/>
      <!-- handle slot -->
      <path class="cut-line" d="M1044,500 V540 Q1044,556 1060,556 H1188 Q1204,556 1204,540 V500"/>
      <line class="cut-line" x1="1124" y1="556" x2="1124" y2="602"/>
      <!-- fold lines -->
      <line class="fold-line" x1="291" y1="397" x2="1318" y2="397"/>
      <line class="fold-line" x1="291" y1="648" x2="1318" y2="648"/>
      <line class="fold-line" x1="291" y1="203" x2="291" y2="648"/>
      <line class="fold-line" x1="930" y1="203" x2="930" y2="648"/>
      <line class="fold-line" x1="1318" y1="180" x2="1318" y2="648"/>
      <!-- base flap -->
      <path class="cut-line" d="M291,648 V873 Q291,893 311,893 H590 Q610,893 610,873 V842 H905 Q928,842 928,820 V710 L906,668 L930,648"/>
      <line class="fold-line" x1="737" y1="842" x2="930" y2="648"/>
      <line class="fold-line" x1="291" y1="648" x2="291" y2="873"/>
      <!-- side base flap -->
      <polyline class="cut-line" points="930,648 982,790 1175,790 1318,648"/>
    </g>
  </defs>

  <!-- front panel A -->
  <g class="panel panel-front">
    <rect class="top-band" x="291" y="203" width="639" height="194"/>
    <rect class="check-band" x="291" y="600" width="639" height="48" role="img" aria-label="Red and white checkered band"/>
    <rect class="mascot-area" x="412" y="345" width="172" height="215" rx="40" role="img" aria-label="Chef rooster mascot giving a thumbs up"/>
    <text class="brand-name" x="596" y="440">GOLDEN</text>
    <text class="brand-name" x="596" y="515">BITE</text>
  </g>

  <!-- front panel B -->
  <g class="panel panel-back">
    <rect class="top-band" x="1318" y="180" width="638" height="217"/>
    <rect class="check-band" x="1318" y="600" width="638" height="48" role="img" aria-label="Red and white checkered band"/>
    <rect class="mascot-area" x="1439" y="345" width="172" height="215" rx="40" role="img" aria-label="Chef rooster mascot giving a thumbs up"/>
    <text class="brand-name" x="1623" y="440">GOLDEN</text>
    <text class="brand-name" x="1623" y="515">BITE</text>
  </g>

  <!-- keyline -->
  <use href="#keyline-half"/>
  <g transform="translate(1027 0)">
    <polyline class="cut-line" points="930,180 978,203 1315,203 1315,648"/>
    <polyline class="fold-line" points="930,397 1124,203 1315,397"/>
    <path class="cut-line" d="M1044,500 V540 Q1044,556 1060,556 H1188 Q1204,556 1204,540 V500"/>
    <line class="cut-line" x1="1124" y1="556" x2="1124" y2="602"/>
    <line class="fold-line" x1="291" y1="397" x2="1315" y2="397"/>
    <line class="fold-line" x1="291" y1="648" x2="1315" y2="648"/>
    <line class="fold-line" x1="291" y1="180" x2="291" y2="648"/>
    <line class="fold-line" x1="930" y1="180" x2="930" y2="648"/>
    <path class="cut-line" d="M291,648 V873 Q291,893 311,893 H590 Q610,893 610,873 V842 H905 Q928,842 928,820 V710 L906,668 L930,648"/>
    <line class="fold-line" x1="737" y1="842" x2="930" y2="648"/>
    <polyline class="cut-line" points="930,648 982,790 1175,790 1315,650"/>
  </g>
</svg>
</body>
</html>
```